Prairie Reading Guild - Minds Charged Website

We need a website designed for a PR + Marketing Campaign (Minds Charged: That's How We Roll) for the Prairie Reading Guild (PRG), the largest statewide library association in the country.

The final design should communicate an empowerment to libraries, its innovative practices, and how they are helping and improving the lives of all communities (of all ages, backgrounds, experiences).

The look should be bold, captivating; meanwhile also simple, clean, easy-to-navigate.

LAYOUT (five pages total):
Page 1: Home – Intro
Animated logo transitioning into simple landing page.
Must feature #chargedshelves and eventually featuring video.

Page 2: About the Campaign
Graphics/photos optional, text below:
Broad Objectives and Goals
Minds Charged: That’s How We Roll seeks to broaden the awareness of library services to the public and provide resources to librarians working in the state in order to promote libraries as vital, technology-centered institutions in the community.
The campaign provides a platform for the sharing of ideas and resources that strengthen the image of the library profession and the services provided by libraries in Texas.
Related goals include: providing librarians with the tools necessary to influence key supporters, shifting the perspectives of libraries as a center for books to a center for emerging technology and the cultivation of ideas, and spreading the message of the campaign through both traditional and social media outlets.
Librarians and information professionals are encouraged to actively participate in the campaign through social media outlets, using the hashtag #chargedshelves, and by contributing content in the Minds Swapped portion of the campaign website.

Page 3: Toolkit – downloadable items
Downloadable Campaign Materials for library professionals
Buttons leading to subpages or one large page covering the topics below

Page 4: Minds Swapped: What We Do: Interactive element page
Toolkit
Here are the tools and downloadable materials for #chargdshelves everywhere. Use these campaign designs to showcase the innovation happening in your library! Check back as we continue to update this page with new content.
Logos
Campaign logos in various formats for use on your own customized designs.
Print Materials
Flyers, bookmarks, posters and more!
Web & Interactive
Graphics for social media and the Web.
Coming soon: #chargedshelves campaign video!
PR & Marketing
Sample press releases, emails, and customizable content for a variety of library types: school, academic, public, and special.

Page 5: Contact Us Page
Can either be a sub-section of the About Us page, or a stand-alone link.
Standard submission form with the ability to upload documents for the Minds Swapped section.
Contact Us
Have a question or comment? Want to contribute a summary and photos or video of your innovative programs for the Minds Swapped section? Please get in touch!
NAME:
EMAIL:
PHONE:
ADDRESS: ?
MESSAGE:
ATTACHMENTS (upload)

MUST HAVE:
-Maintain the color-scheme of the logo (attached)
-The WEBSITE design must innovation and excitement. a contemporary design/layout that demonstrates vitality
-Somewhere on every page, we would like an interactive element for viewers, such as a stream from Chatterbook/Flutterly with hashtags.
-Countdown to Campaign Launch
-Can we include animation? We are striving to create movement with the abstract icon in our log.

PLEASE AVOID:
-NO pastels, NO soft colors, nothing that might be considered feminine (pinks, etc); we do want to stear away from stereotypes (NO books, NO library buildings, NO reading conceptual designs) and standard icons (NO lightbulbs and NO lightning designs)

AUDIENCE/MARKET:
THE PUBLIC (also includes all kinds of librarians and their supporters: information, reference, school, public, special, law, academic, students, educators, administration, support staff, lay and advocates)

AUDIENCE/MARKET:

• The final design should communicate an empowerment to libraries, its innovative practices, and how they are helping and improving the lives of all communities (of all ages, backgrounds, experiences).
• The look should be bold, captivating; meanwhile also simple, clean, easy-to-navigate.
• LAYOUT (five pages total):
• Page 1: Home – Intro
• Animated logo transitioning into simple landing page.
• Must feature #chargedshelves and eventually featuring video.
• Page 2: About the Campaign
• Graphics/photos optional, text below:
• Broad Objectives and Goals
• Minds Charged: That’s How We Roll seeks to broaden the awareness of library services to the public and provide resources to librarians working in the state in order to promote libraries as vital, technology-centered institutions in the community.
• The campaign provides a platform for the sharing of ideas and resources that strengthen the image of the library profession and the services provided by libraries in Texas.
• Related goals include: providing librarians with the tools necessary to influence key supporters, shifting the perspectives of libraries as a center for books to a center for emerging technology and the cultivation of ideas, and spreading the message of the campaign through both traditional and social media outlets.
• Librarians and information professionals are encouraged to actively participate in the campaign through social media outlets, using the hashtag #chargedshelves, and by contributing content in the Minds Swapped portion of the campaign website.
• Page 3: Toolkit – downloadable items
• Downloadable Campaign Materials for library professionals
• Buttons leading to subpages or one large page covering the topics below
• Page 4: Minds Swapped: What We Do: Interactive element page
• Toolkit
• Here are the tools and downloadable materials for #chargdshelves everywhere. Use these campaign designs to showcase the innovation happening in your library! Check back as we continue to update this page with new content.
• Logos
• Campaign logos in various formats for use on your own customized designs.
• Print Materials
• Flyers, bookmarks, posters and more!
• Web & Interactive
• Graphics for social media and the Web.
• Coming soon: #chargedshelves campaign video!
• PR & Marketing
• Sample press releases, emails, and customizable content for a variety of library types: school, academic, public, and special.
• Page 5: Contact Us Page
• Can either be a sub-section of the About Us page, or a stand-alone link.
• Standard submission form with the ability to upload documents for the Minds Swapped section.
• Contact Us
• Have a question or comment? Want to contribute a summary and photos or video of your innovative programs for the Minds Swapped section? Please get in touch!
• NAME:
• EMAIL:
• PHONE:
• ADDRESS: ?
• MESSAGE:
• ATTACHMENTS (upload)
• MUST HAVE:
• -Maintain the color-scheme of the logo (attached)
• -The WEBSITE design must innovation and excitement. a contemporary design/layout that demonstrates vitality
• -Somewhere on every page, we would like an interactive element for viewers, such as a stream from Chatterbook/Flutterly with hashtags.
• -Countdown to Campaign Launch
• -Can we include animation? We are striving to create movement with the abstract icon in our log.
• PLEASE AVOID:
• -NO pastels, NO soft colors, nothing that might be considered feminine (pinks, etc); we do want to stear away from stereotypes (NO books, NO library buildings, NO reading conceptual designs) and standard icons (NO lightbulbs and NO lightning designs)

```html
<!DOCTYPE html>
<html lang="en">
<head>
<meta charset="utf-8">
<title>Minds Charged – That's How We Roll</title>
<link href="https://fonts.googleapis.com/css2?family=Roboto:wght@300;400;500&display=swap" rel="stylesheet">
<style>
:root{
  --blue:#29a8e0;
  --ink:#222;
  --muted:#666;
  --grey:#777;
  --white:#fff;
  --line:#ccc;
}
*{box-sizing:border-box;margin:0;padding:0}
html,body{width:1200px;height:1086px;overflow:hidden;background:var(--white)}
body{font-family:'Roboto',Arial,sans-serif;color:var(--ink);position:relative}

.site-header{position:absolute;left:0;top:0;width:1200px;height:110px}
.brand{position:absolute;left:74px;top:30px;display:flex;align-items:center;gap:10px}
.brand-mark{width:26px;height:26px;border:3px solid var(--blue);border-radius:4px}
.brand-name{font-size:19px;font-weight:500;color:var(--blue);line-height:1.1}
.brand-tag{font-size:10px;letter-spacing:2.5px;color:var(--blue);text-transform:uppercase;margin-top:3px}
.main-nav{position:absolute;right:76px;top:52px;display:flex;gap:44px;font-size:15px}
.main-nav a{color:var(--ink);text-decoration:none}
.main-nav a.is-current{color:var(--blue);border:3px solid var(--blue);border-radius:4px;padding:6px 10px;margin:-9px -13px}

.hero{position:absolute;left:0;top:110px;width:1200px;height:464px;border-bottom:3px solid var(--blue);
  background:linear-gradient(100deg,#dfe8ec 0%,#c9d9e2 40%,#b9ced9 60%,#aec4d0 100%)}
.hero-photo{position:absolute;left:520px;top:0;width:680px;height:461px;
  background:radial-gradient(ellipse at 60% 55%,#7d8486 0%,#9aa9b1 35%,rgba(174,196,208,0) 70%)}
.hero-copy{position:absolute;left:74px;top:103px;width:425px}
.hero-title{font-size:40px;font-weight:400;line-height:45px;color:var(--ink)}
.hero-title .plus{color:var(--blue)}
.hero-text{margin-top:28px;font-size:15px;line-height:22px;text-align:justify;color:var(--ink)}
.slider-dots{display:flex;gap:6px;margin-top:22px}
.slider-dots span{width:12px;height:12px;border-radius:50%;background:var(--white)}
.slider-dots span.is-active{background:var(--ink)}

.section-title{font-size:23px;font-weight:400;color:var(--grey);letter-spacing:.5px;text-transform:uppercase}
.section-title em{font-style:normal;color:var(--blue)}

.libraries{position:absolute;left:74px;top:630px;width:582px}
.libraries .section-title{padding-bottom:12px;border-bottom:1px dashed var(--line)}
.libraries p{margin-top:14px;font-size:13.4px;line-height:24px;color:var(--muted);text-align:justify;font-weight:400}
.read-more{display:inline-flex;align-items:center;gap:8px;margin-top:10px;font-size:14px;color:var(--blue);text-decoration:none}

.video{position:absolute;left:704px;top:630px;width:422px}
.video-frame{margin-top:12px;border:1px solid #ddd;padding:4px;background:var(--white);box-shadow:0 0 3px rgba(0,0,0,.1)}
.video-still{position:relative;height:266px;background:linear-gradient(120deg,#c9cfd2 0%,#7f878b 45%,#5c6468 100%)}
.play-btn{position:absolute;left:175px;top:82px}
.video-bar{position:absolute;left:0;bottom:0;width:100%;height:38px;background:#222;display:flex;align-items:center;padding:0 14px;gap:10px}
.progress{flex:1;height:4px;background:#777;margin-left:10px;position:relative}
.progress i{position:absolute;left:0;top:0;height:4px;width:19%;background:#e0312f}

.site-footer{position:absolute;left:0;top:980px;width:1200px;height:106px;background:var(--blue);color:var(--white)}
.social{position:absolute;left:76px;top:28px;display:flex;gap:14px;font-size:12px}
.social span{display:flex;align-items:center;gap:5px}
.social span::before{content:"";width:12px;height:12px;border:2px solid var(--white);border-radius:50%}
.copyright{position:absolute;left:76px;top:68px;font-size:13.5px}
.partner{position:absolute;right:74px;top:36px;display:flex;align-items:center;gap:12px;font-size:14px;text-align:right;line-height:19px}
.partner-badge{width:34px;height:28px;background:rgba(255,255,255,.85)}
</style>
</head>
<body>
<header class="site-header">
  <div class="brand">
    <span class="brand-mark"></span>
    <div>
      <div class="brand-name">Minds Charged</div>
      <div class="brand-tag">That's How We Roll</div>
    </div>
  </div>
  <nav class="main-nav">
    <a class="is-current" href="#">Home</a>
    <a href="#">About the Campaign</a>
    <a href="#">Toolkit</a>
    <a href="#">Minds swapped</a>
    <a href="#">Contact us</a>
  </nav>
</header>

<section class="hero">
  <div class="hero-photo" role="img" aria-label="Photo of a young man shouting into a megaphone against a cloudy sky filled with flying letters"></div>
  <div class="hero-copy">
    <h1 class="hero-title">PR <span class="plus">+</span> Marketing<br>Campaign Company</h1>
    <p class="hero-text">PR &amp; Marketing Committee with the task of creating a big campaign to raise awareness about Texas libraries and the library profession in general, which would have wide appeal to all types of libraries</p>
    <div class="slider-dots"><span></span><span></span><span class="is-active"></span></div>
  </div>
</section>

<section class="libraries">
  <h2 class="section-title">Powered <em>Libraries</em></h2>
  <p>Lorem Ipsum is simply dummy text of the printing and typesetting industry. Lorem Ipsum has been the industry's standard dummy text ever since the 1500s, when an unknown printer took a galley of type and scrambled it to make a type specimen book. It has survived not only five centuries, but also the leap into electronic typesetting, remaining essentially unchanged. It was popularised in the 1960s with the release of Lettrafix sheets containing Lorem Ipsum passages, and more recently with desktop publishing software like Quillset PageForge including. It was popularised in the 1960s with the release of Lettrafix sheets containing Lorem Ipsum passages, and more recently with desktop publishing software like Quillset PageForge including. It was popularised in the 1960s with the release of Lettrafix sheets containing Lorem Ipsum passages, and more.</p>
  <a class="read-more" href="#">READ MORE
    <svg width="14" height="14" viewBox="0 0 14 14" aria-hidden="true"><circle cx="7" cy="7" r="6" fill="none" stroke="currentColor" stroke-width="1.5"/><path d="M4 7h5M7 4.5 9.5 7 7 9.5" fill="none" stroke="currentColor" stroke-width="1.5"/></svg>
  </a>
</section>

<section class="video">
  <h2 class="section-title">Featuring <em>Video</em></h2>
  <div class="video-frame">
    <div class="video-still" role="img" aria-label="Video still of hands touching a tablet with floating technology cubes">
      <svg class="play-btn" width="70" height="70" viewBox="0 0 70 70" aria-hidden="true"><circle cx="35" cy="35" r="32" fill="rgba(255,255,255,.15)" stroke="#fff" stroke-width="3"/><path d="M28 23v24l18-12z" fill="none" stroke="#fff" stroke-width="2"/></svg>
      <div class="video-bar">
        <svg width="10" height="12" viewBox="0 0 10 12" aria-hidden="true"><path d="M0 0v12l10-6z" fill="#fff"/></svg>
        <svg width="10" height="12" viewBox="0 0 10 12" aria-hidden="true"><rect width="3.5" height="12" fill="#fff"/><rect x="6.5" width="3.5" height="12" fill="#fff"/></svg>
        <div class="progress"><i></i></div>
      </div>
    </div>
  </div>
</section>

<footer class="site-footer">
  <div class="social"><span>Chatterbook</span><span>Flutterly</span><span>Circleplus</span><span>Pictogrid</span></div>
  <p class="copyright">© 2015, Minds Charged: That's How We Roll, All Right Reserved</p>
  <div class="partner">
    <span>Prairie Reading<br>Guild</span>
    <span class="partner-badge"></span>
  </div>
</footer>
</body>
</html>
```